Ember Ridge Lodge website (design only)

Ember Ridg Lodge (http://www.emberridgemw.com) is a private Safari lodge located in Malawi.
We would like a modern, professional website designed that does not subscribe to the cliched view of a Safari in Africa, but still maintain a wildlife/safari atmosphere.

The aim of our website is to entice people & drive them to the booking form.

Here are some examples of websites that we like. Although we would like our site to be a bit more in line with modern web design trends.

http://www.tolukora.com/
http://www.varembo.com/
http://www.pelomavuto.com/

Requirements
Must have
• Here is a list of the pages required. Most of them will follow a standard content layout. I.e. heading, body and images.

If you take a look at the website, you will get an idea of hoe many page types there are +- 5

http://www.emberridgemw.com/index.htm

About Ember Ridge
Kotelo Country Club
Rooms
Conferences
Cuisine
Facilities
Your Safari
Activities
Rates & Special Offers
Booking form
Latest Developments
How To Get There
Gallery
Contact Us
Blog / Newsfeed

```html
<!DOCTYPE html>
<html lang="en">
<head>
<meta charset="utf-8">
<title>Ember Ridge Lodge</title>
<link href="https://fonts.googleapis.com/css2?family=Arimo:wght@400;700&family=Kaushan+Script&family=Roboto+Condensed:wght@700&display=swap" rel="stylesheet">
<style>
:root{
  --night:#1d1715;
  --night-top:#181211;
  --night-line:#2c2421;
  --orange:#f7941d;
  --orange-deep:#e0780f;
  --orange-light:#fdb042;
  --white:#ffffff;
  --paper:#ffffff;
  --ink:#3d3d3d;
  --ink-soft:#555555;
  --heading:#5a5a5a;
  --rust:#c8400f;
  --green:#7ab51d;
  --green-dark:#5e9412;
  --brown:#3a1e12;
  --footer:#383533;
  --frame:#d0d0d0;
  --grey-btn:#b8b5b3;
}
*{margin:0;padding:0;box-sizing:border-box}
html,body{width:1200px;height:945px;overflow:hidden;background:var(--paper)}
body{position:relative;font-family:"Arimo",Arial,sans-serif;color:var(--ink)}
.hero{position:absolute;left:0;top:0;width:1200px;height:504px;
  background:linear-gradient(180deg,var(--night) 0%,#221a17 60%,var(--night) 100%);
  border-bottom:3px solid var(--orange-deep)}
.topbar{position:absolute;left:0;top:0;width:1200px;height:96px;background:var(--night-top);border-bottom:1px solid var(--night-line)}
.brand{position:absolute;left:213px;top:26px;display:flex;align-items:center;gap:12px}
.brand-mark{width:40px;height:40px;border-radius:50%;background:var(--orange)}
.brand-name{font-family:"Arimo",Arial,sans-serif;font-weight:700;font-size:27px;color:var(--white)}
.top-nav{position:absolute;left:545px;top:68px;display:flex;gap:14px;list-style:none}
.top-nav li{font-family:"Kaushan Script",cursive;font-size:15px;color:var(--white)}
.top-nav li.current{color:var(--orange);text-decoration:underline}
.top-nav li.contact{margin-left:10px}
.ribbon{position:absolute;left:202px;top:115px;width:801px;height:37px}
.ribbon svg{position:absolute;left:0;top:0}
.ribbon-nav{position:absolute;left:30px;top:0;height:37px;display:flex;align-items:center;gap:0;list-style:none}
.ribbon-nav li{font-weight:700;font-size:14px;color:var(--white);text-shadow:0 1px 1px rgba(0,0,0,.35);margin-right:22px}
.arrow{position:absolute;top:296px;width:26px;height:26px;border-radius:50%;background:var(--white)}
.arrow svg{display:block}
.arrow-prev{left:224px}
.arrow-next{left:954px}
.slide{position:absolute;background:var(--white);border-radius:5px;box-shadow:0 3px 10px rgba(0,0,0,.5)}
.slide-side{top:219px;width:180px;height:193px}
.slide-left{left:265px}
.slide-right{left:760px;width:167px}
.slide-photo{position:absolute}
.slide-left .slide-photo{left:7px;top:7px;width:173px;height:138px;background:linear-gradient(160deg,#7c9ab8 0%,#c9b9a3 40%,#3d7a3a 75%,#b63030 100%)}
.slide-right .slide-photo{left:15px;top:7px;width:143px;height:138px;background:linear-gradient(150deg,#a2542a 0%,#d08a4a 45%,#7a2b1e 80%,#3c2a1f 100%)}
.slide-main{left:443px;top:185px;width:332px;height:275px;z-index:2}
.slide-main .slide-photo{left:7px;top:7px;width:318px;height:204px;background:linear-gradient(160deg,#6a5a4a 0%,#8f7a5c 30%,#5f8f3a 60%,#3c7a2a 100%)}
.slide-caption{position:absolute;left:20px;top:227px;display:flex;align-items:baseline;gap:6px}
.slide-caption .label{font-family:"Kaushan Script",cursive;font-size:18px;color:var(--orange)}
.slide-caption .price{font-weight:700;font-size:11px;color:#333}
.details-btn{position:absolute;left:257px;top:227px;width:66px;height:28px;border-radius:3px;
  background:linear-gradient(180deg,#8cc63f,var(--green-dark));color:var(--white);
  font-family:Georgia,"Times New Roman",serif;font-style:italic;font-size:14px;display:flex;align-items:center;justify-content:center}
.content{position:absolute;left:0;top:507px;width:1200px;height:340px}
.promo{position:absolute;left:200px;width:181px;height:123px;border:1px solid var(--frame);padding:3px;background:var(--white)}
.promo-safari{top:24px}
.promo-booking{top:162px}
.promo-fill{position:relative;width:100%;height:100%}
.promo-safari .promo-fill{background:linear-gradient(135deg,#c9a468 0%,#dcc08a 45%,#a78248 100%)}
.promo-booking .promo-fill{background:linear-gradient(180deg,#1f4fa0 0%,#3d4f7a 45%,#7a4a22 75%,#2c1a12 100%)}
.promo-title{position:absolute;font-size:13.5px}
.promo-safari .promo-title{left:6px;top:6px;color:#5a2a0a}
.promo-booking .promo-title{right:6px;top:6px;color:var(--white);text-align:right;line-height:1.3}
.welcome{position:absolute;left:404px;top:24px;width:375px}
.welcome h1{font-weight:400;font-size:19px;color:var(--heading);margin-bottom:10px}
.welcome p{font-size:10.4px;line-height:14.4px;color:var(--ink-soft);text-align:justify}
.welcome p + p{margin-top:14px}
.read-more{position:absolute;left:404px;top:266px;width:65px;height:21px;border-radius:3px;background:var(--brown);
  color:var(--white);font-size:10px;display:flex;align-items:center;justify-content:center}
.updates{position:absolute;left:813px;top:25px;width:190px}
.updates h2{font-family:"Roboto Condensed",Arial,sans-serif;font-weight:700;font-size:16.5px;color:var(--heading);margin-bottom:10px}
.update{margin-bottom:12px;padding-left:3px}
.update h3{font-size:10px;font-weight:700;color:var(--rust);margin-bottom:9px}
.update p{font-size:10px;line-height:14.6px;color:var(--ink);text-align:justify}
.more-btn{display:inline-flex;margin-top:4px;width:49px;height:17px;background:linear-gradient(180deg,#cfcccb,var(--grey-btn));
  color:var(--white);font-size:10px;align-items:center;justify-content:center}
.site-footer{position:absolute;left:0;top:847px;width:1200px;height:98px;background:var(--footer)}
.site-footer p{position:absolute;left:202px;font-size:9.5px;color:var(--white)}
.copyright{top:18px}
.terms{top:42px}
</style>
</head>
<body>

<header class="hero">
  <div class="topbar">
    <div class="brand">
      <span class="brand-mark"></span>
      <span class="brand-name">Ember Ridge Lodge</span>
    </div>
    <ul class="top-nav">
      <li class="current">About us</li>
      <li>Conferences</li>
      <li>Facilities</li>
      <li>Rates &amp; Special Offers</li>
      <li class="contact">Contact Us</li>
    </ul>
  </div>

  <nav class="ribbon">
    <svg width="801" height="37" viewBox="0 0 801 37">
      <defs>
        <linearGradient id="ribbonFill" x1="0" y1="0" x2="0" y2="1">
          <stop offset="0" stop-color="#fdb042"/>
          <stop offset="1" stop-color="#f08c12"/>
        </linearGradient>
      </defs>
      <polygon points="0,0 801,0 784,18.5 801,37 0,37 17,18.5" fill="url(#ribbonFill)"/>
    </svg>
    <ul class="ribbon-nav">
      <li>Cuisine</li>
      <li>Rooms</li>
      <li>Your Safari</li>
      <li>Activities</li>
      <li>Booking Rrequests</li>
      <li>How To Get There</li>
      <li>Gallery</li>
      <li>Our Blog</li>
    </ul>
  </nav>

  <div class="arrow arrow-prev">
    <svg width="26" height="26" viewBox="0 0 26 26"><path d="M15 8 L10 13 L15 18" fill="none" stroke="#333" stroke-width="3" stroke-linecap="round" stroke-linejoin="round"/></svg>
  </div>
  <div class="arrow arrow-next">
    <svg width="26" height="26" viewBox="0 0 26 26"><path d="M11 8 L16 13 L11 18" fill="none" stroke="#333" stroke-width="3" stroke-linecap="round" stroke-linejoin="round"/></svg>
  </div>

  <div class="slide slide-side slide-left">
    <div class="slide-photo" role="img" aria-label="Lodge buildings with green roofs among flower gardens and hills"></div>
  </div>
  <div class="slide slide-side slide-right">
    <div class="slide-photo" role="img" aria-label="Warm lodge lounge with red sofas and wooden ceiling"></div>
  </div>
  <div class="slide slide-main">
    <div class="slide-photo" role="img" aria-label="Antlered deer grazing on grass beside rocks and a stream"></div>
    <div class="slide-caption">
      <span class="label">Lorem</span>
      <span class="price">Ipsum $ 200</span>
    </div>
    <div class="details-btn">Details</div>
  </div>
</header>

<main class="content">
  <div class="promo promo-safari">
    <div class="promo-fill" role="img" aria-label="Antelope standing in golden grassland">
      <span class="promo-title">Your Safari</span>
    </div>
  </div>
  <div class="promo promo-booking">
    <div class="promo-fill" role="img" aria-label="Lodge entrance lit up at dusk">
      <span class="promo-title">Enquire For<br>Booking</span>
    </div>
  </div>

  <section class="welcome">
    <h1>Welcome to Ember Ridge Lodge</h1>
    <p>Warmest welcome to the unique Malawi experience. lodge complex, game park, the 18 hole Kotelo golf club and Nsewa dam.</p>
    <p>A multi million dollar development at Lusenga estate, Mpalika on Kalinde road 20 kms from Blantyre Malawi's commercial capital creating a fascinating paradise for multiple leisure activities and conserving Malawi wildlife.Our Lodge also has beautifully designed and built in golden colored rock.<br>
    The 1st phase was completed in 2007, and is approx 1800 sq. meters, comprising of:<br>
    A fully carpeted and elegantly furnished restaurant with seating for up to 80 guests and exceptional cuisine to completely satisfy most palates.<br>
    A stately carpeted conference hall for up to 45 people, 5 luxurious and spacious ensuite cottages with lounge and private verandah accessing a beautiful 18 meter swimming pool with cascading waterfall.</p>
  </section>
  <div class="read-more">Read more</div>

  <aside class="updates">
    <h2>Ember Ridge Updates</h2>
    <div class="update">
      <h3>Project Development</h3>
      <p>The 2nd phase commenced in February 2011 and consists of:-<br>Construction of an international 18 hole golf course by Dravenko</p>
      <span class="more-btn">more</span>
    </div>
    <div class="update">
      <h3>Safari</h3>
      <p>We have supplemented our game park with indigenous Malawi wild life which consists of sable, waterbuck, zebra, impala, wildebeest, nyala, giraffe and numerous duiker and smaller wild cats and otters.</p>
      <span class="more-btn">more</span>
    </div>
  </aside>
</main>

<footer class="site-footer">
  <p class="copyright">Copyright © 2011 Ember Ridge Pty Ltd</p>
  <p class="terms">Terms of Services</p>
</footer>

</body>
</html>
```